Harbouring Dawn Rituals creates individual, personalised ceremonies to celebrate weddings, naming days,coming of age, significant age, divorce and final resting rites. Ceremonies and meaningful rituals are created in collaboration with the individual to reflect their hopes and desires, how they will/have embrace/d their lives. The final design should have the logo (purple) on a white/silver background on the right hand side of the card. Name of business and contact details in red on a black background on the left
Updates

Hi All, have only just realised I have paid for a double sided card, yep, a newbie! Sorry to set the cat amongst the pigeons but could we put 'creating...... etc' on the back?

Target Market(s)

Couples marrying, renewing of vows, baby naming days, coming of age, significant age, divorce, funeral ceremonies. The target market predominantly will be couples marrying.

Industry/Entity Type

Business

Contact Information for Business Card

Harbouring Dawn Rituals, Doriane Whitcombe, 0428-735902 harbouringdawnrituals1@examplemail.test
"Shaping singular, tailored rituals harbouring dawn"

Font styles to use
Script

Colors
eb1f27
6b449b
f3f0f8

Requirements
Must have
• On initial entry, and now, the logo was not displayed in full - the bottom part was cut off - this needs to be in it's entirety. Colours as previously specified are non-negotiable. Font and placement of characters will be assessed as produced.
Should not have
• Telephone symbol, call us, director,grammatical symbols ( : )

```html
<!DOCTYPE html>
<html lang="en">
<head>
<meta charset="utf-8">
<title>Harbouring Dawn Rituals – Business Card</title>
<link rel="stylesheet" href="https://fonts.googleapis.com/css2?family=Pinyon+Script&family=Crimson+Text&display=swap">
<style>
  :root {
    --page-bg: #ffffff;
    --card-dark: #231f20;
    --card-dark-soft: #2c2829;
    --card-light: #f3f0f8;
    --accent-red: #eb1f27;
    --accent-purple: #6b449b;
    --card-shadow: rgba(0, 0, 0, 0.18);
  }
  html, body {
    margin: 0;
    padding: 0;
    width: 1200px;
    height: 784px;
    overflow: hidden;
    background: var(--page-bg);
  }
  .business-card {
    position: absolute;
    left: 232px;
    top: 162px;
    width: 748px;
    height: 430px;
    display: flex;
    box-shadow: 0 1px 3px var(--card-shadow);
  }
  .card-front {
    position: relative;
    width: 501px;
    height: 100%;
    background: var(--card-dark);
    overflow: hidden;
  }
  .pattern-fill {
    position: absolute;
    inset: 0;
    background: linear-gradient(135deg, var(--card-dark-soft), var(--card-dark) 60%, var(--card-dark-soft));
  }
  .business-name {
    position: absolute;
    left: 20px;
    top: 42px;
    margin: 0;
    font-family: "Pinyon Script", cursive;
    font-weight: 400;
    font-size: 42px;
    color: var(--accent-red);
    white-space: nowrap;
  }
  .contact {
    position: absolute;
    left: 25px;
    top: 290px;
    font-family: "Crimson Text", serif;
    color: var(--accent-red);
  }
  .contact-name {
    margin: 0 0 8px;
    font-size: 25px;
  }
  .contact-phone,
  .contact-email {
    margin: 0 0 11px;
    font-size: 18px;
  }
  .card-back {
    position: relative;
    flex: 1;
    background: var(--card-light);
    text-align: center;
  }
  .brand-mark {
    position: absolute;
    left: 0;
    right: 0;
    top: 40px;
    display: flex;
    flex-direction: column;
    align-items: center;
    gap: 14px;
  }
  .brand-dot {
    width: 72px;
    height: 72px;
    border-radius: 50%;
    background: var(--accent-purple);
  }
  .brand-name {
    margin: 0;
    width: 200px;
    font-family: "Pinyon Script", cursive;
    font-size: 32px;
    line-height: 1.05;
    color: var(--accent-purple);
  }
  .tagline {
    position: absolute;
    left: 0;
    right: 0;
    top: 318px;
    margin: 0;
    font-family: "Pinyon Script", cursive;
    font-size: 22px;
    line-height: 28px;
    color: var(--accent-purple);
  }
</style>
</head>
<body>
  <div class="business-card">
    <section class="card-front">
      <div class="pattern-fill" role="img" aria-label="Faint dark grey repeating flourish pattern behind the card front"></div>
      <h1 class="business-name">Harbouring Dawn Rituals</h1>
      <div class="contact">
        <p class="contact-name">Doriane Whitcombe</p>
        <p class="contact-phone">0428-735902</p>
        <p class="contact-email">harbouringdawnrituals1@examplemail.test</p>
      </div>
    </section>
    <section class="card-back">
      <div class="brand-mark">
        <span class="brand-dot"></span>
        <p class="brand-name">Harbouring Dawn Rituals</p>
      </div>
      <p class="tagline">“ Shaping singular,<br>tailored rituals<br>harbouring dawn”</p>
    </section>
  </div>
</body>
</html>
```